Real Estate Investment Company Needs A Business Card Designed

I need a business card designed for my use. We are a real estate investment company based in Omaha, Nebraska that specializes in buying, rehabbing and selling single family and multifamily properties. Would love designs that incorporate our logo and colors

Industry/Entity Type

Business

Contact Information for Business Card

Mitchell Parkhurst | President & CEO
4873 North 52nd Avenue, Ste 700
Omaha, NE 68142
(402) 786-4259
mitchell@kestrelgateproperties.example
www.KestrelgateProperties.example

Font styles to use
Serif

Colors
0255a3
3276b5

Requirements
Must have
• Our logo

```html
<!DOCTYPE html>
<html lang="en">
<head>
<meta charset="utf-8">
<title>Kestrelgate Properties – Business Card</title>
<link rel="stylesheet" href="https://fonts.googleapis.com/css2?family=Lato:wght@400;700;900&display=swap">
<style>
  :root {
    --brand-deep: #0255a3;
    --brand-mid: #3276b5;
    --brand-light: #4f95d6;
    --ink-grey: #9aa3ad;
    --card-white: #ffffff;
    --stage: #3a3b3d;
  }
  * { box-sizing: border-box; margin: 0; padding: 0; }
  html, body { width: 1200px; height: 900px; overflow: hidden; }
  body {
    background: var(--stage);
    font-family: "Lato", Arial, sans-serif;
    position: relative;
  }
  .card {
    position: absolute;
    width: 640px;
    height: 366px;
    border-radius: 24px;
    overflow: hidden;
    box-shadow: 0 14px 30px rgba(0,0,0,.45);
  }
  /* Front */
  .card-front {
    left: 200px; top: 60px;
    background: linear-gradient(135deg, var(--brand-mid) 0%, var(--brand-deep) 70%);
    display: flex; flex-direction: column; align-items: center; justify-content: center;
  }
  .card-front .brand-mark {
    width: 70px; height: 70px; border-radius: 50%;
    background: rgba(255,255,255,.22);
    margin-bottom: 14px;
  }
  .card-front .brand-name {
    color: var(--card-white);
    font-weight: 900; font-size: 26px; letter-spacing: 1px; text-transform: uppercase;
  }
  /* Back */
  .card-back {
    left: 360px; top: 470px;
    background: var(--card-white);
  }
  .back-brand {
    position: absolute; right: 40px; top: 40px;
    display: flex; align-items: center; gap: 10px;
  }
  .back-brand .brand-mark {
    width: 34px; height: 34px; border-radius: 50%; background: var(--brand-mid);
  }
  .back-brand .brand-name {
    color: var(--brand-deep); font-weight: 900; font-size: 20px; text-transform: uppercase; letter-spacing: .5px;
  }
  .holder { position: absolute; left: 44px; top: 120px; }
  .holder-name { color: var(--brand-deep); font-weight: 900; font-size: 19px; }
  .holder-title { color: var(--brand-mid); font-weight: 700; font-size: 17px; margin-top: 2px; }
  .contacts { position: absolute; left: 44px; top: 190px; list-style: none; }
  .contacts li {
    display: flex; align-items: center; gap: 8px;
    color: var(--brand-deep); font-size: 15px; line-height: 22px;
  }
  .contacts svg { width: 15px; height: 15px; flex: none; }
  .address { position: absolute; left: 44px; top: 268px; color: var(--brand-deep); font-size: 15.5px; line-height: 21px; }
  .band {
    position: absolute; left: 0; right: 0; bottom: 0; height: 46px;
    background: linear-gradient(90deg, var(--brand-deep), var(--brand-mid));
    display: flex; align-items: center; gap: 8px; padding-left: 44px;
  }
  .band .social { width: 18px; height: 18px; border-radius: 4px; background: var(--card-white); }
</style>
</head>
<body>
  <section class="card card-front" aria-label="Card front">
    <div class="brand-mark"></div>
    <div class="brand-name">Kestrelgate Properties</div>
  </section>

  <section class="card card-back" aria-label="Card back">
    <div class="back-brand">
      <div class="brand-mark"></div>
      <div class="brand-name">Kestrelgate Properties</div>
    </div>

    <div class="holder">
      <div class="holder-name">Mitchell Parkhurst</div>
      <div class="holder-title">President &amp; CEO</div>
    </div>

    <ul class="contacts">
      <li>
        <svg viewBox="0 0 16 16"><rect x="0" y="0" width="16" height="16" rx="3" fill="var(--brand-mid)"/><path d="M4 5c0 4 3 7 7 7l1-2-2-1-1 1c-1-.5-2-1.5-2.5-2.5l1-1-1-2z" fill="#fff"/></svg>
        (402) 786-4259
      </li>
      <li>
        <svg viewBox="0 0 16 16"><rect x="0" y="0" width="16" height="16" rx="3" fill="var(--brand-mid)"/><rect x="3.5" y="5" width="9" height="6" fill="none" stroke="#fff" stroke-width="1.2"/><path d="M3.5 5l4.5 3.5L12.5 5" fill="none" stroke="#fff" stroke-width="1.2"/></svg>
        mitchell@kestrelgateproperties.example
      </li>
      <li>
        <svg viewBox="0 0 16 16"><rect x="0" y="0" width="16" height="16" rx="3" fill="var(--brand-mid)"/><circle cx="8" cy="8" r="4.5" fill="none" stroke="#fff" stroke-width="1.1"/><ellipse cx="8" cy="8" rx="2" ry="4.5" fill="none" stroke="#fff" stroke-width="1"/><path d="M3.5 8h9" stroke="#fff" stroke-width="1"/></svg>
        www.KestrelgateProperties.example
      </li>
    </ul>

    <address class="address" style="font-style:normal">
      4873 North 52nd Avenue, Ste 700<br>
      Omaha, NE 68142
    </address>

    <div class="band">
      <span class="social" role="img" aria-label="Social profile"></span>
      <span class="social" role="img" aria-label="Social profile"></span>
      <span class="social" role="img" aria-label="Social profile"></span>
    </div>
  </section>
</body>
</html>
```